Zia Lotte's Sweet Kitchen

I would like a website to tell the story of our cookies as well as products to sell. We make Pizzelle's from our Great Grandmothers cookie recipe. Our original product is Vanilla Pizzelle's but we have added other flavors as well as products. These are an italian Tradition and would like the logo be represented in the design

Target Market(s)

Dessert Lovers, Coffee/Tea drinkers, Italians, gifts

Industry/Entity Type

Baked goods, cookies

Coding

Colors
59FF00
82FF00
B8FF75
E3FFCB
F4FFEA
F0912C
F2A743
F7CA91
FBE8D2
FDF5EE
EB3D1F
EC4F4E
F09395
F8D3D4
FCEDEE

Requirements
Must have
• My logo, About Page, Products, ordering page
Nice to have
• I have uploaded my logo and Product labels so you can get an idea of colors and fonts

```html
<!DOCTYPE html>
<html lang="en">
<head>
<meta charset="utf-8">
<title>Zia Lotte's Sweet Kitchen</title>
<link rel="stylesheet" href="https://fonts.googleapis.com/css2?family=Dancing+Script:wght@700&family=Lora:wght@400&family=Poppins:wght@400;500;600&display=swap">
<style>
:root{
  --orange:#e07a2e;
  --orange-soft:#f0912c;
  --peach:#f7ca91;
  --cream:#faefe7;
  --ink:#111111;
  --text:#2b2b2b;
  --grey:#b5b5b5;
  --white:#ffffff;
  --dark-ring:#3a1c0c;
}
*{margin:0;padding:0;box-sizing:border-box}
html,body{width:1200px;height:3032px;overflow:hidden;background:var(--white)}
body{position:relative;font-family:'Lora',serif;color:var(--text)}
.abs{position:absolute}
.script{font-family:'Dancing Script',cursive;font-weight:700}

/* header */
.site-header{top:0;left:0;width:1200px;height:85px;background:var(--white);z-index:5}
.nav-link{top:34px;font-family:'Poppins',sans-serif;font-size:15.5px;color:var(--ink)}
.nav-link.active{color:var(--orange);border-bottom:1.5px solid var(--orange);padding-bottom:2px}
.brand-badge{left:517px;top:0;width:192px;height:176px;border-radius:0 0 96px 96px;background:var(--white);box-shadow:0 4px 10px rgba(0,0,0,.12);z-index:6;display:flex;flex-direction:column;align-items:center;justify-content:center;gap:10px;text-align:center;padding-top:10px}
.brand-dot{width:14px;height:14px;border-radius:50%;background:var(--orange)}
.brand-name{font-family:'Poppins',sans-serif;font-weight:500;color:var(--orange);font-size:17px;line-height:1.25;width:130px}

/* hero */
.hero{top:85px;left:0;width:1200px;height:660px;overflow:hidden}
.hero-photo{position:absolute;inset:0;background:
  linear-gradient(180deg,rgba(0,0,0,0) 60%,rgba(0,0,0,.05) 100%),
  linear-gradient(100deg,#aaa5a1 0%,#b7b1ac 48%,#8e5a32 58%,#b47a45 66%,#c58c52 74%,#e3c866 84%,#bfb9b3 93%,#aea9a5 100%)}
.hero-title{left:98px;top:128px;font-size:86px;line-height:90px;color:var(--white)}
.hero-text{left:98px;top:320px;width:400px;font-size:15.5px;line-height:31px;color:var(--white)}
.btn{display:flex;align-items:center;justify-content:center;background:var(--orange);color:var(--white);font-family:'Poppins',sans-serif;font-weight:600;font-size:16px;border-radius:26px 4px 26px 4px;box-shadow:3px 4px 0 rgba(0,0,0,.12)}
.hero-btn{left:98px;top:400px;width:137px;height:52px}
.slider-dot{left:1138px;width:12px;height:12px;border-radius:50%;background:var(--orange)}
.slider-dot.current{background:var(--white)}
.hero-wave{position:absolute;left:0;bottom:0}

/* about */
.about-mark{left:98px;top:790px;width:418px;height:500px;display:flex;flex-direction:column;align-items:center;justify-content:center;gap:26px;text-align:center}
.about-mark-dot{width:64px;height:64px;border-radius:50%;background:var(--orange)}
.about-mark-name{font-family:'Poppins',sans-serif;font-weight:500;font-size:56px;line-height:1.12;color:var(--orange)}
.section-title{font-size:56px;color:var(--ink)}
.section-title span{color:var(--orange)}
.about-title{left:569px;top:790px}
.about-text{left:569px;top:861px;width:525px;font-size:15.6px;line-height:30.8px;color:var(--text)}
.about-btn{left:569px;top:1220px;width:138px;height:51px}

/* flavors */
.flavors{top:1378px;left:0;width:1200px;height:585px;background:var(--cream)}
.flavors-title{left:0;width:1200px;text-align:center;top:52px;font-size:46px}
.flavor-ring{top:145px}
.flavor-photo{position:absolute;border-radius:50%}
.flavor-name{top:492px;width:200px;text-align:center;font-size:29px;color:var(--ink)}

/* reviews */
.reviews-title{left:0;width:1200px;text-align:center;top:2018px;font-size:46px}
.review-card{top:2107px;width:468px;height:273px;background:var(--white);box-shadow:0 3px 14px rgba(0,0,0,.12)}
.reviewer-photo{position:absolute;left:24px;top:30px;width:102px;height:102px;border-radius:50%}
.reviewer-name{position:absolute;left:148px;top:36px;font-family:'Poppins',sans-serif;font-weight:500;font-size:19px;color:var(--ink)}
.reviewer-role{position:absolute;left:148px;top:68px;font-family:'Poppins',sans-serif;font-size:14px;color:var(--ink)}
.stars{position:absolute;left:284px;top:70px;color:var(--orange-soft);font-size:13px;letter-spacing:1px}
.source-dot{position:absolute;right:36px;top:38px;width:24px;height:24px;border-radius:50%;border:4px solid #4a7fe0}
.review-text{position:absolute;left:149px;top:98px;width:290px;font-size:15.5px;line-height:30px;color:var(--text)}
.review-text b{color:var(--orange);font-weight:400}
.quote-mark{position:absolute;left:32px;top:138px;font-family:'Lora',serif;font-size:150px;color:#f3cfb4;line-height:1}
.card-corner{position:absolute;right:0;bottom:0;width:21px;height:18px;background:var(--orange)}
.slide-arrow{top:2221px;width:35px;height:35px;border-radius:50%;border:1.5px solid #9a9a9a;display:flex;align-items:center;justify-content:center}

/* footer */
.footer{top:2440px;left:0;width:1200px;height:592px}
.footer-black{position:absolute;left:0;top:110px;width:1200px;height:482px;background:var(--ink)}
.footer-brand{left:95px;top:2650px;width:188px;height:215px;display:flex;flex-direction:column;align-items:center;justify-content:center;gap:14px;text-align:center}
.footer-brand-dot{width:34px;height:34px;border-radius:50%;background:var(--orange)}
.footer-brand-name{font-family:'Poppins',sans-serif;font-weight:500;color:var(--orange);font-size:26px;line-height:1.15}
.social{top:2883px;width:30px;height:30px;background:var(--orange)}
.footer-heading{top:2692px;font-family:'Poppins',sans-serif;font-weight:600;font-size:21px;color:var(--white)}
.quick-links{left:338px;top:2730px;list-style:none;font-size:15.5px;line-height:30.8px;color:var(--white)}
.contact-row{left:520px;display:flex;align-items:center;gap:13px;font-size:15.5px;color:var(--white)}
.contact-icon{width:37px;height:37px;border-radius:50%;background:var(--white);display:flex;align-items:center;justify-content:center}
.touch-text{left:847px;top:2732px;font-size:15.5px;color:var(--white)}
.subscribe{left:847px;top:2790px;width:252px;height:44px;display:flex}
.subscribe-field{flex:1;background:var(--white);border:1px solid #ddd;font-size:15.5px;color:#444;display:flex;align-items:center;padding-left:15px}
.subscribe-btn{width:43px;background:var(--orange);display:flex;align-items:center;justify-content:center}
.footer-rule{left:98px;top:2968px;width:1004px;height:1px;background:#777}
.copyright{left:0;top:2987px;width:1200px;text-align:center;font-size:15.5px;color:var(--white)}
</style>
</head>
<body>

<header class="abs site-header">
  <span class="abs nav-link active" style="left:140px">Home</span>
  <span class="abs nav-link" style="left:238px">About Us</span>
  <span class="abs nav-link" style="left:356px">Services</span>
  <span class="abs nav-link" style="left:770px">Flavors</span>
  <span class="abs nav-link" style="left:874px">Reviews</span>
  <span class="abs nav-link" style="left:985px">Contact Us</span>
</header>
<div class="abs brand-badge">
  <span class="brand-dot"></span>
  <span class="brand-name">Zia Lotte's Sweet Kitchen</span>
</div>

<section class="abs hero">
  <div class="hero-photo" role="img" aria-label="Stacked rolled pizzelle cookies in chocolate, plain and vanilla with scattered chocolate chips"></div>
  <h1 class="abs hero-title script">Welcome To<br>Zia Lotte's</h1>
  <p class="abs hero-text">Lorem ipsum dolor sit amet, consectetur adipiscing elit, sed do eiusmod dolore magna aliqua.</p>
  <span class="abs btn hero-btn">Get Started</span>
  <span class="abs slider-dot current" style="top:267px"></span>
  <span class="abs slider-dot" style="top:292px"></span>
  <span class="abs slider-dot" style="top:317px"></span>
  <svg class="hero-wave" width="1200" height="140" viewBox="0 0 1200 140">
    <path d="M0 100 C200 30 420 10 620 45 C820 80 950 150 1200 55 L1200 140 L0 140Z" fill="var(--orange)"/>
    <path d="M0 118 C200 48 420 30 620 66 C820 102 960 168 1200 78 L1200 140 L0 140Z" fill="var(--white)"/>
  </svg>
</section>

<section>
  <div class="abs about-mark">
    <span class="about-mark-dot"></span>
    <span class="about-mark-name">Zia Lotte's<br>Sweet Kitchen</span>
  </div>
  <h2 class="abs section-title about-title script">About <span>Us</span></h2>
  <p class="abs about-text">Sed ut perspiciatis unde omnis iste natus error sit voluptatem accusantium doloremque laudantium, totam rem aperiam, eaque ipsa quae ab illo inventore veritatis et quasi architecto beatae vitae dicta sunt explicabo. Nemo enim ipsam voluptatem quia voluptas sit aspernatur aut odit aut fugit, sed quia consequuntur magni dolores eos qui ratione voluptatem sequi nesciunt. Neque porro quisquam est, qui dolorem ipsum quia dolor sit amet, consectetur, adipisci velit, sed quia non numquam eius modi tempora incidunt ut labore et dolore magnam aliquam quaerat voluptatem. Ut enim ad minima veniam, quis nostrum exercitationem ullam corporis suscipit laboriosam, nisi ut aliquid ex ea commodi consequatur?</p>
  <span class="abs btn about-btn">Read More</span>
</section>

<section class="abs flavors">
  <h2 class="abs section-title flavors-title script">Our <span>Flavors</span></h2>

  <svg class="abs flavor-ring" style="left:98px" width="332" height="332" viewBox="0 0 332 332">
    <circle cx="166" cy="166" r="163" fill="none" stroke="var(--dark-ring)" stroke-width="2"/>
    <path d="M3 166 A163 163 0 0 1 238 19" fill="none" stroke="var(--orange)" stroke-width="2.5"/>
    <circle cx="166" cy="166" r="140" fill="none" stroke="var(--orange-soft)" stroke-width="2"/>
    <circle cx="222" cy="27" r="5" fill="var(--ink)"/><circle cx="166" cy="306" r="5" fill="var(--ink)"/>
    <circle cx="298" cy="70" r="5" fill="var(--orange)"/><circle cx="12" cy="220" r="5" fill="var(--orange)"/>
  </svg>
  <div class="flavor-photo" style="left:131px;top:177px;width:268px;height:268px;background:linear-gradient(180deg,#e8e4e1 0%,#c8443c 22%,#a9322f 34%,#c48d5c 46%,#ecebea 62%,#e1ddda 100%)" role="img" aria-label="Vanilla pizzelle cup filled with strawberries on a white stand"></div>
  <span class="abs flavor-name script" style="left:164px">Vanilla</span>

  <svg class="abs flavor-ring" style="left:435px" width="332" height="332" viewBox="0 0 332 332">
    <circle cx="166" cy="166" r="163" fill="none" stroke="var(--dark-ring)" stroke-width="2"/>
    <path d="M3 166 A163 163 0 0 1 238 19" fill="none" stroke="var(--orange)" stroke-width="2.5"/>
    <circle cx="166" cy="166" r="140" fill="none" stroke="var(--orange-soft)" stroke-width="2"/>
    <circle cx="222" cy="27" r="5" fill="var(--ink)"/><circle cx="166" cy="306" r="5" fill="var(--ink)"/>
    <circle cx="298" cy="70" r="5" fill="var(--orange)"/><circle cx="12" cy="220" r="5" fill="var(--orange)"/>
  </svg>
  <div class="flavor-photo" style="left:468px;top:177px;width:268px;height:268px;background:linear-gradient(160deg,#ebe8e5 0%,#d9b79a 22%,#c08a5e 45%,#b07a50 65%,#e4dfdb 86%,#ecebea 100%)" role="img" aria-label="Chocolate pizzelle dusted with sugar among chocolate chips"></div>
  <span class="abs flavor-name script" style="left:500px">Chocolate</span>

  <svg class="abs flavor-ring" style="left:772px" width="332" height="332" viewBox="0 0 332 332">
    <circle cx="166" cy="166" r="163" fill="none" stroke="var(--dark-ring)" stroke-width="2"/>
    <path d="M3 166 A163 163 0 0 1 238 19" fill="none" stroke="var(--orange)" stroke-width="2.5"/>
    <circle cx="166" cy="166" r="140" fill="none" stroke="var(--orange-soft)" stroke-width="2"/>
    <circle cx="222" cy="27" r="5" fill="var(--ink)"/><circle cx="166" cy="306" r="5" fill="var(--ink)"/>
    <circle cx="298" cy="70" r="5" fill="var(--orange)"/><circle cx="12" cy="220" r="5" fill="var(--orange)"/>
  </svg>
  <div class="flavor-photo" style="left:805px;top:177px;width:268px;height:268px;background:linear-gradient(180deg,#e6e6e8 0%,#e6e6e8 18%,#e5bb6e 30%,#d9a75a 44%,#e7dcc9 54%,#f1f1f3 70%,#dcdde0 100%)" role="img" aria-label="Chai pizzelle stacked on a white cake stand"></div>
  <span class="abs flavor-name script" style="left:837px">Chai</span>
</section>

<h2 class="abs section-title reviews-title script">Our <span>Reviews</span></h2>

<span class="abs slide-arrow" style="left:36px"><svg width="12" height="16" viewBox="0 0 12 16"><path d="M9 1 L3 8 L9 15" fill="none" stroke="#888" stroke-width="1.6"/></svg></span>
<span class="abs slide-arrow" style="left:1131px"><svg width="12" height="16" viewBox="0 0 12 16"><path d="M3 1 L9 8 L3 15" fill="none" stroke="#888" stroke-width="1.6"/></svg></span>

<article class="abs review-card" style="left:112px">
  <div class="reviewer-photo" style="background:linear-gradient(180deg,#8fbbe0 0%,#5f93c6 45%,#1f4f8f 100%)" role="img" aria-label="Reviewer portrait"></div>
  <span class="reviewer-name">Dana Whitlock</span>
  <span class="reviewer-role">Lorem Ipsum set</span>
  <span class="stars">★★★★★</span>
  <span class="source-dot"></span>
  <span class="quote-mark">“</span>
  <p class="review-text">Nemo enim ipsam voluptatem quia voluptas sit aspernatur aut odit aut fugit, sed quia consequuntur magni dolores eos qui ratione voluptatem sequi nesciunt <b>»</b></p>
  <span class="card-corner"></span>
</article>

<article class="abs review-card" style="left:621px">
  <div class="reviewer-photo" style="background:linear-gradient(180deg,#bfe3f0 0%,#5bb0c8 45%,#2b6f85 70%,#2a2a2a 100%)" role="img" aria-label="Reviewer portrait"></div>
  <span class="reviewer-name">Dana Whitlock</span>
  <span class="reviewer-role">Lorem Ipsum set</span>
  <span class="stars">★★★★★</span>
  <span class="source-dot"></span>
  <span class="quote-mark">“</span>
  <p class="review-text">Nemo enim ipsam voluptatem quia voluptas sit aspernatur aut odit aut fugit, sed quia consequuntur magni dolores eos qui ratione voluptatem sequi nesciunt <b>»</b></p>
  <span class="card-corner"></span>
</article>

<footer class="abs footer">
  <svg class="abs" style="left:0;top:0" width="1200" height="130" viewBox="0 0 1200 130">
    <path d="M0 95 C220 20 420 0 640 40 C860 80 1000 120 1200 15 L1200 130 L0 130Z" fill="var(--orange)"/>
    <path d="M0 112 C220 42 420 26 640 66 C860 108 1010 150 1200 48 L1200 130 L0 130Z" fill="var(--ink)"/>
  </svg>
  <div class="footer-black"></div>
</footer>

<div class="abs footer-brand">
  <span class="footer-brand-dot"></span>
  <span class="footer-brand-name">Zia Lotte's<br>Sweet Kitchen</span>
</div>
<span class="abs social" style="left:116px"></span>
<span class="abs social" style="left:166px"></span>
<span class="abs social" style="left:213px"></span>

<h3 class="abs footer-heading" style="left:338px">Quick Links</h3>
<ul class="abs quick-links">
  <li>Home</li><li>About Us</li><li>Menu</li><li>Order Online</li><li>What's New</li><li>Contact Us</li>
</ul>

<h3 class="abs footer-heading" style="left:520px">Contact Us</h3>
<div class="abs contact-row" style="top:2734px">
  <span class="contact-icon"><svg width="12" height="16" viewBox="0 0 12 16"><path d="M6 0 A6 6 0 0 1 12 6 C12 10 6 16 6 16 C6 16 0 10 0 6 A6 6 0 0 1 6 0Z" fill="var(--ink)"/><circle cx="6" cy="6" r="2.2" fill="#fff"/></svg></span>
  <span>Zia Lotte's, United States.</span>
</div>
<div class="abs contact-row" style="top:2794px">
  <span class="contact-icon"><svg width="15" height="11" viewBox="0 0 15 11"><rect width="15" height="11" rx="1.5" fill="var(--ink)"/><path d="M1 1.5 L7.5 6 L14 1.5" fill="none" stroke="#fff" stroke-width="1.2"/></svg></span>
  <span>info@zialottes.com</span>
</div>
<div class="abs contact-row" style="top:2854px">
  <span class="contact-icon"><svg width="14" height="14" viewBox="0 0 24 24"><path d="M6.6 10.8a15.1 15.1 0 0 0 6.6 6.6l2.2-2.2c.3-.3.7-.4 1-.2 1.1.4 2.3.6 3.6.6.6 0 1 .4 1 1V20c0 .6-.4 1-1 1C10.6 21 3 13.4 3 4c0-.6.4-1 1-1h3.5c.6 0 1 .4 1 1 0 1.3.2 2.5.6 3.6.1.3 0 .7-.2 1z" fill="var(--ink)"/></svg></span>
  <span>+1 555 014 2299</span>
</div>

<h3 class="abs footer-heading" style="left:847px">Get In Touch</h3>
<p class="abs touch-text">Lorem ipsum dolor sit amet</p>
<div class="abs subscribe">
  <span class="subscribe-field">Email Address</span>
  <span class="subscribe-btn"><svg width="16" height="16" viewBox="0 0 16 16"><path d="M15 1 L1 7 L7 9 L9 15Z" fill="#fff"/></svg></span>
</div>

<div class="abs footer-rule"></div>
<p class="abs copyright">Copyrights@2023.Company Name.All Rights Reserved</p>

</body>
</html>
```